Yard signs to bring awareness to the neighborhood we are here to help you also.

My project is to build brand awareness in a Neighborhood before during and after my company's get a home owner approve from there in insurance Approved to replace there roof due to the recent storms. Call us we can do the same for you.
We are trying to let the neighborhood know that they may also have enough storm damage for them to have there roof and gutters replace at no cost to them. And we can help with there claim to go over all the steps involved.

Target Market(s)

Brand awareness to Home owner in the neighborhood

Industry/Entity Type

Roofing

Font styles to use
Sans Serif

Requirements
Must have
• Insurance Approved
Wind & Hail
Call For Free consultation
612 459-2817
Nice to have
• Make phone # big and bold

```html
<!DOCTYPE html>
<html lang="en">
<head>
<meta charset="utf-8">
<title>J&amp;M Roofing LLC. – Wind &amp; Hail Yard Sign</title>
<link rel="stylesheet" href="https://fonts.googleapis.com/css2?family=Archivo+Black&family=Oswald:wght@600&family=Montserrat:wght@800&family=Allura&display=swap">
<style>
  :root {
    --page-bg: #d4d4d4;
    --ink-dark: #12121c;
    --roof-teal: #00c7a0;
    --mint: #80fce0;
    --script-teal: #1fcfa4;
    --pill-blue: #1f3c8a;
    --white: #ffffff;
    --photo-top: #8d9096;
    --photo-bottom: #5c5d62;
  }
  * { box-sizing: border-box; margin: 0; padding: 0; }
  html, body { width: 1200px; height: 1200px; overflow: hidden; }
  body { background: var(--page-bg); position: relative; }

  .yard-sign {
    position: absolute;
    left: 253px; top: 79px;
    width: 694px; height: 1042px;
    background: var(--ink-dark);
    overflow: hidden;
  }
  .storm-photo {
    position: absolute; left: 0; top: 0;
    width: 694px; height: 400px;
    background: linear-gradient(160deg, var(--photo-top) 0%, #76787d 50%, var(--photo-bottom) 100%);
  }
  .roof-shape { position: absolute; left: 0; top: 0; width: 694px; height: 1042px; }

  .headline {
    position: absolute; left: 0; width: 694px; top: 30px;
    text-align: center;
    font-family: 'Archivo Black', sans-serif;
    color: var(--white);
    font-size: 112px; line-height: 100px;
    letter-spacing: -1px;
  }
  .company-name {
    position: absolute; left: 83px; top: 404px;
    font-family: 'Oswald', sans-serif; font-weight: 600;
    color: var(--mint);
    font-size: 86px; line-height: 96px;
    letter-spacing: -1px;
    white-space: nowrap;
    transform: scaleX(0.89);
    transform-origin: left center;
  }
  .brand-mark {
    position: absolute; left: 56px; top: 546px;
    display: flex; align-items: center; gap: 6px;
    font-family: 'Oswald', sans-serif; font-weight: 600;
    color: var(--roof-teal);
    font-size: 44px; line-height: 64px;
  }
  .brand-mark .dot {
    width: 16px; height: 16px; border-radius: 50%;
    background: var(--roof-teal);
  }
  .tagline {
    position: absolute; left: 152px; top: 546px;
    font-family: 'Allura', cursive;
    color: var(--script-teal);
    font-size: 58px; line-height: 52px;
    white-space: nowrap;
  }
  .tagline span { display: block; }
  .tagline .second { padding-left: 68px; }

  .phone-band { position: absolute; left: 0; top: 731px; width: 694px; height: 166px; }
  .phone-number {
    position: absolute; left: 0; width: 694px; top: 760px;
    text-align: center;
    font-family: 'Archivo Black', sans-serif;
    color: var(--ink-dark);
    font-size: 86px; line-height: 90px;
    white-space: nowrap;
  }
  .consult-pill {
    position: absolute; left: 53px; top: 859px;
    width: 587px; height: 59px;
    border-radius: 16px;
    background: var(--pill-blue);
    display: flex; align-items: center; justify-content: center;
    font-family: 'Montserrat', sans-serif; font-weight: 800;
    color: var(--white);
    font-size: 42px; letter-spacing: 1px;
  }
  .insurance-line {
    position: absolute; left: 0; width: 694px; top: 942px;
    text-align: center;
    font-family: 'Oswald', sans-serif; font-weight: 600;
    color: var(--mint);
    font-size: 62px; line-height: 68px;
    letter-spacing: 3px;
    word-spacing: 6px;
    white-space: nowrap;
  }
</style>
</head>
<body>
  <main class="yard-sign">
    <div class="storm-photo" role="img" aria-label="Photo of a two-storey house with a storm-damaged, partly collapsed shingle roof and trees behind"></div>

    <svg class="roof-shape" viewBox="0 0 694 1042" aria-hidden="true">
      <polygon points="0,386 348,247 694,380 694,400 0,400" fill="var(--roof-teal)"/>
      <polygon points="0,388 348,271 694,384 694,1042 0,1042" fill="var(--ink-dark)"/>
    </svg>

    <h1 class="headline">WIND &amp;<br>HALL</h1>

    <h2 class="company-name">J&amp;M ROOFING LLC.</h2>

    <div class="brand-mark"><span class="dot"></span>J&amp;M</div>

    <p class="tagline">
      <span>Nobody Does it Better!</span>
      <span class="second">Here To Serve.</span>
    </p>

    <svg class="phone-band" viewBox="0 0 694 166" aria-hidden="true">
      <polygon points="0,0 329,0 348,17 367,0 694,0 694,166 0,166" fill="var(--mint)"/>
    </svg>

    <p class="phone-number">612 459-2817</p>

    <div class="consult-pill">FREE CONSULTATION</div>

    <p class="insurance-line">INSURANCE APPROVED</p>
  </main>
</body>
</html>
```